COMMERCIAL OFFICE FOR SALE- Brochure, Miami, FL 33131

BROCHURE DESIGN BRIEF – COMMERCIAL OFFICE FOR SALE

I need a clean, modern brochure for a commercial office listing (FOR SALE, not lease). This will be used both digitally (email + SpanDesk/attachments) and printed if needed.

Please follow a “Sample Flyer Copy” style layout — strong headline, clean sections, minimal clutter, and easy to scan. Use fints Seasons and Poppins interchangeably.

All property details, specs, and exact wording should be pulled directly from the MLS Listing file I provided. Do not guess or rewrite specs.

OVERALL LOOK + FEEL

Clean, high-end, professional (Brickell / financial district vibe)

Think: simple, sharp, not busy

Neutral palette (white, black, soft gray) + subtle accent color if needed

Prioritize readability over design gimmicks

Plenty of white space

FORMAT

1-page flyer (primary)

Also format so it can easily convert into a 2-page version if needed

PDF optimized for email + print

HEADER SECTION (TOP OF PAGE)

Large, strong headline:

Example: “Office Condo for Sale | Brickell” (adjust based on MLS info)

Subheadline (smaller):

Key positioning (corner unit, square footage, etc.)

Include 1 strong hero image (best photo of the unit)

PROPERTY OVERVIEW (RIGHT UNDER HEADER OR NEXT BLOCK)

Clean bullet section with icons if possible:

Include:

Total square footage

Layout highlights (conference room, offices, open workspace, etc.)

Kitchen / breakroom

Reception area

Storage / printer room

Floor or suite number

Any standout feature (corner unit, natural light, views, etc.)

Keep this tight and clean — no long paragraphs.

PRICING SECTION

Clearly state: FOR SALE

Price (from MLS)

Price per square foot

Make this visually stand out.

LOCATION SECTION

Short and clean:

Building name + address

1–2 lines max on location advantages (Brickell, access, etc.)

Optional small map if it fits cleanly

ADDITIONAL DETAILS (IF SPACE ALLOWS)

Building amenities (if relevant)

Parking info

Zoning / permitted uses (if applicable)

Only include what is confirmed in MLS.

IMAGES

3–5 total max

Keep it clean — do not overcrowd

Prioritize:

Main workspace

Conference room

Kitchen

Any standout feature

CONTACT SECTION (VERY IMPORTANT – EXACT FORMAT)

This must be clean and prominent.

Colette Varnum
REALTOR®
Tamsworth Lindale HomePartners QRF Realty

Phone: [your number]
Email: [your email]

Call to action line:

“For more information or to schedule a private showing, contact Colette Varnum.”

Include my business card details (office location etc.) in this section.

BROKERAGE + LOGOS

Use TLHP QRF Realty logos provided

Place cleanly (bottom or footer)

Do not distort or restyle logos

FOOTER

Standard disclaimer if needed

Keep minimal

IMPORTANT NOTES

This is a SALE listing — do not use the word lease anywhere

Do not overdesign — clean always wins

Keep everything aligned and balanced

Make sure spacing feels high-end, not cramped
Updates

Please include this video link within the document: https://vidshare.example/kQ7pTzR2vNa?ref=hx4Lm9Ys_Wd2Pc8E

State: Step inside. Watch the full video tour. and hyperlink Watch with the link

Target Market(s)

Buyers, Professionals, Lawyer Office, Family Office, Small FInancial Offices

Industry/Entity Type

Commercial Real Estate

Font styles to use
Serif
Sans Serif

Requirements
Must have
• Clean, clear, layout and good imagery
Should not have
• Professional flow, follow my font guidlines and thebrochure i shared as a guide

```html
<!DOCTYPE html>
<html lang="en">
<head>
<meta charset="utf-8">
<title>Office Condo for Sale – Brickell</title>
<link href="https://fonts.googleapis.com/css2?family=Playfair+Display:wght@400;500&family=Poppins:wght@400;500;600;700&display=swap" rel="stylesheet">
<style>
:root{
  --stage:#c4c4c4;
  --paper:#ffffff;
  --navy:#13284a;
  --ink:#1b1f27;
  --muted:#4a4f58;
  --mist:#eef1f6;
  --tile:#f4f5f8;
  --tile-line:#dde1e8;
  --rule:#cfd4dc;
}
*{box-sizing:border-box;margin:0;padding:0}
html,body{width:1200px;height:1137px;overflow:hidden;background:var(--stage)}
body{position:relative;font-family:"Poppins",sans-serif;color:var(--ink)}
.sheet{position:absolute;top:203px;width:540px;height:699px;background:var(--paper)}
.sheet--one{left:46px}
.sheet--two{left:612px}
.title{position:absolute;left:0;right:0;text-align:center;font-family:"Playfair Display",serif;color:var(--ink);font-weight:400}
.title__kicker{top:18px;font-size:26px;letter-spacing:.5px}
.title__place{top:48px;font-size:36px;letter-spacing:3px}
.band{position:absolute;left:13px;width:514px;display:flex;align-items:center;justify-content:center;font-size:12.5px;font-weight:500}
.band--specs{top:96px;height:22px;background:var(--mist);color:var(--ink);gap:12px}
.band--address{top:120px;height:22px;background:var(--navy);color:#fff;font-size:11px}
.intro{position:absolute;left:20px;top:166px;width:292px;font-size:9.5px;line-height:1.45;color:var(--muted)}
.section-head{position:absolute;left:20px;top:226px;font-family:"Playfair Display",serif;font-weight:400;font-size:15px;letter-spacing:1.8px;color:var(--navy)}
.tiles{position:absolute;left:18px;top:262px;display:grid;grid-template-columns:repeat(3,90px);grid-auto-rows:100px;gap:8px}
.tile{background:var(--tile);border:1px solid var(--tile-line);display:flex;flex-direction:column;align-items:center;justify-content:flex-end;padding:0 6px 12px;text-align:center;font-size:9px;color:var(--muted);line-height:1.25;text-transform:uppercase}
.tile svg{margin-bottom:auto;margin-top:14px}
.tile__figure{font-size:15px;font-weight:700;color:var(--ink)}
.tile__wrap{max-width:62px}
.tile--price{background:var(--navy);border-color:var(--navy);color:#fff;justify-content:center;padding:0}
.tile--price .price-label{font-family:"Playfair Display",serif;font-size:14px;letter-spacing:1px}
.tile--price .price-value{font-weight:700;font-size:11px;text-transform:none}
.tile--price .price-rate{font-size:10px;text-transform:none}
.features{position:absolute;left:20px;top:488px;list-style:none;font-size:9.5px;line-height:1.3;color:var(--ink)}
.features li::before{content:"• "}
.hero{position:absolute;left:323px;top:155px;width:204px;height:382px;background:linear-gradient(180deg,#6fa3d8 0%,#8cb8e0 30%,#3d6c8e 60%,#2f5a44 100%)}
.cta{position:absolute;left:13px;top:551px;width:514px}
.cta__bar{height:22px;background:var(--navy);color:#fff;font-size:12px;font-weight:600;display:flex;align-items:center;justify-content:center;letter-spacing:.3px}
.cta__bar a{color:#fff;text-decoration:none}
.cta__link{height:26px;background:var(--mist);display:flex;align-items:center;justify-content:center;font-size:9px;color:var(--ink)}
.footer{position:absolute;left:13px;top:608px;width:514px;height:82px}
.brand{position:absolute;left:12px;top:20px;display:flex;align-items:center;gap:6px;font-size:11px;font-weight:500;color:var(--ink);white-space:nowrap}
.brand__mark{width:8px;height:8px;background:var(--navy)}
.brand__site{position:absolute;left:12px;top:58px;font-size:8.5px;font-weight:600;color:var(--navy);letter-spacing:.4px}
.divider{position:absolute;left:170px;top:6px;width:1px;height:68px;background:var(--rule)}
.invite{position:absolute;left:190px;top:6px;width:230px;font-family:"Playfair Display",serif;font-size:9.5px;line-height:1.3}
.agent{position:absolute;left:190px;top:38px;font-size:8.5px;line-height:1.35}
.agent strong{font-weight:600}
.reach{position:absolute;left:354px;top:38px;list-style:none;font-size:8.5px;line-height:1.35}
.reach li{display:flex;gap:5px;align-items:flex-start}
.reach svg{flex:none;margin-top:2px}
.plan{position:absolute;left:29px;top:166px;width:312px;height:188px;background:linear-gradient(135deg,#f7f7f7,#e4e4e4)}
.details{position:absolute;left:356px;top:166px;width:161px;height:194px;background:var(--tile);padding:14px 16px;font-size:9px;line-height:1.3;color:var(--muted)}
.details h3{font-size:9.5px;font-weight:700;color:var(--ink);margin-bottom:10px;letter-spacing:.3px}
.details dt{font-weight:600;color:var(--ink)}
.details dd{margin-bottom:8px}
.gallery{position:absolute;top:375px;height:90px}
.gallery--work{left:12px;width:160px;background:linear-gradient(180deg,#e9e9e6 0%,#cfcfcb 55%,#7c7f83 100%)}
.gallery--meeting{left:188px;width:155px;background:linear-gradient(180deg,#ecebe6 0%,#d7d2c6 55%,#8a6a4c 100%)}
.gallery--kitchen{left:357px;width:160px;background:linear-gradient(180deg,#efe8dc 0%,#c7a883 55%,#5f564e 100%)}
.summary{position:absolute;left:40px;right:40px;top:480px;text-align:center;font-size:9.5px;line-height:1.4;color:var(--muted)}
</style>
</head>
<body>

<section class="sheet sheet--one">
  <h1 class="title title__kicker">OFFICE CONDO FOR SALE</h1>
  <h2 class="title title__place">BRICKELL</h2>
  <div class="band band--specs"><span>MOVE-IN READY</span><span>|</span><span>2,146 SF</span><span>|</span><span>CORNER UNIT OFFICE SUITE</span></div>
  <div class="band band--address">1280 BAYLINE AVENUE, SUITE 712-C MIAMI, FL 33131</div>

  <p class="intro">Positioned in the heart of Brickell’s central business district with immediate access to major corridors, dining, and retail including Marlow Square Village and Crescent City Centre.</p>
  <h3 class="section-head">PROPERTY OVERVIEW</h3>

  <div class="tiles">
    <div class="tile">
      <svg width="30" height="30" viewBox="0 0 30 30" fill="none" stroke="#1b1f27" stroke-width="1.4"><rect x="6" y="6" width="18" height="18"/><circle cx="6" cy="6" r="2.5" fill="#fff"/><circle cx="24" cy="6" r="2.5" fill="#fff"/><circle cx="6" cy="24" r="2.5" fill="#fff"/><circle cx="24" cy="24" r="2.5" fill="#fff"/></svg>
      <span class="tile__figure">2,146 SF</span><span>OFFICE SUITE</span>
    </div>
    <div class="tile">
      <svg width="34" height="30" viewBox="0 0 34 30" fill="none" stroke="#1b1f27" stroke-width="1.4"><rect x="3" y="18" width="28" height="9"/><path d="M11 18a6 6 0 0 1 12 0"/><line x1="17" y1="10" x2="17" y2="12"/><line x1="12" y1="12" x2="22" y2="12"/></svg>
      <span>RECEPTION<br>AREA</span>
    </div>
    <div class="tile">
      <svg width="30" height="30" viewBox="0 0 30 30" fill="none" stroke="#1b1f27" stroke-width="1.4"><rect x="8" y="3" width="14" height="24"/><circle cx="18" cy="15" r="1" fill="#1b1f27"/><line x1="4" y1="27" x2="26" y2="27"/></svg>
      <span class="tile__wrap"><span class="tile__figure">4</span> PRIVATE OFFICES</span>
    </div>
    <div class="tile">
      <svg width="30" height="30" viewBox="0 0 30 30" fill="none" stroke="#1b1f27" stroke-width="1.4"><rect x="4" y="4" width="22" height="22"/><line x1="15" y1="4" x2="15" y2="26"/><line x1="4" y1="15" x2="26" y2="15"/></svg>
      <span>OPEN<br>WORKSPACE</span>
    </div>
    <div class="tile">
      <svg width="30" height="30" viewBox="0 0 30 30" fill="none" stroke="#1b1f27" stroke-width="1.4"><rect x="10" y="6" width="10" height="18" rx="4"/><circle cx="5" cy="10" r="2.5"/><circle cx="5" cy="20" r="2.5"/><circle cx="25" cy="10" r="2.5"/><circle cx="25" cy="20" r="2.5"/></svg>
      <span>CONFERENCE<br>ROOM</span>
    </div>
    <div class="tile tile--price">
      <span class="price-label">FOR SALE</span>
      <span class="price-value">$1,148,000</span>
      <span class="price-rate">$535 / SF</span>
    </div>
  </div>

  <ul class="features">
    <li>Corner Unit with Natural Light</li>
    <li>Located on Floor 7</li>
    <li>Printer / Copy Room</li>
    <li>Kitchenette • Breakroom</li>
  </ul>

  <div class="hero" role="img" aria-label="Glass office tower against blue sky with palm trees at its base"></div>

  <div class="cta">
    <div class="cta__bar">STEP INSIDE.&nbsp;<a href="https://vidshare.example/kQ7pTzR2vNa?ref=hx4Lm9Ys_Wd2Pc8E">WATCH</a>&nbsp;THE FULL VIDEO TOUR.</div>
    <div class="cta__link">(Hyperlink “Watch” to: https://vidshare.example/kQ7pTzR2vNa?ref=hx4Lm9Ys_Wd2Pc8E)</div>
  </div>

  <footer class="footer">
    <div class="brand"><span class="brand__mark"></span>TLHP QRF Realty</div>
    <div class="brand__site">TAMSWORTHLINDALE.EXAMPLE</div>
    <div class="divider"></div>
    <p class="invite">For more information or to schedule a private showing, contact Colette Varnum.</p>
    <p class="agent"><strong>Colette Varnum</strong><br><strong>REALTOR® License #3851207</strong><br>Tamsworth Lindale HomePartners<br>QRF Realty</p>
    <ul class="reach">
      <li><svg width="8" height="8" viewBox="0 0 10 10"><path d="M2 1l2 2-1 1.5a6 6 0 0 0 2.5 2.5L7 6l2 2-1.5 1.5C4 9 1 6 .5 2.5z" fill="#1b1f27"/></svg>555-208-4417</li>
      <li><svg width="8" height="8" viewBox="0 0 10 10" fill="none" stroke="#1b1f27"><rect x=".5" y="1.5" width="9" height="7"/><path d="M.5 1.5l4.5 4 4.5-4"/></svg>colettevarnum@mailbox.example</li>
      <li><svg width="8" height="8" viewBox="0 0 10 10" fill="none" stroke="#1b1f27"><path d="M5 9.5S1.5 6 1.5 3.8a3.5 3.5 0 0 1 7 0C8.5 6 5 9.5 5 9.5z"/><circle cx="5" cy="4" r="1.2"/></svg>480 Harbor Crest Way<br>Palmera Springs, FL 33902</li>
    </ul>
  </footer>
</section>

<section class="sheet sheet--two">
  <h1 class="title title__kicker">OFFICE CONDO FOR SALE</h1>
  <h2 class="title title__place">BRICKELL</h2>
  <div class="band band--specs"><span>MOVE-IN READY</span><span>|</span><span>2,146 SF</span><span>|</span><span>CORNER UNIT OFFICE SUITE</span></div>
  <div class="band band--address">1280 BAYLINE AVENUE, SUITE 712-C MIAMI, FL 33131</div>

  <div class="plan" role="img" aria-label="Floor plan of Suite 712, 2,146 SF, outlined in red at the corner of the seventh floor"></div>

  <dl class="details">
    <h3>ADDITIONAL DETAILS</h3>
    <dt>Building:</dt><dd>1280 Bayline Condo</dd>
    <dt>Parking:</dt><dd>Covered, Guest &amp;<br>Common Parking</dd>
    <dt>Security:</dt><dd>On-Site Security Guard</dd>
    <dt>Cooling:</dt><dd>Central Building A/C</dd>
  </dl>

  <div class="gallery gallery--work" role="img" aria-label="Open workspace with desk and windows"></div>
  <div class="gallery gallery--meeting" role="img" aria-label="Conference room with oval wooden table"></div>
  <div class="gallery gallery--kitchen" role="img" aria-label="Kitchenette with wood cabinets and stools"></div>

  <p class="summary">Move-in ready office suite in the heart of Brickell with an efficient, functional layout.<br>Features a mix of private offices, open workspace, and a conference room.<br>Located within 1280 Bayline Avenue, offering a professional business setting.<br>Ideal for an owner-user or investor seeking long-term value in a prime location.</p>

  <div class="cta">
    <div class="cta__bar">STEP INSIDE.&nbsp;<a href="https://vidshare.example/kQ7pTzR2vNa?ref=hx4Lm9Ys_Wd2Pc8E">WATCH</a>&nbsp;THE FULL VIDEO TOUR.</div>
    <div class="cta__link">(Hyperlink “Watch” to: https://vidshare.example/kQ7pTzR2vNa?ref=hx4Lm9Ys_Wd2Pc8E)</div>
  </div>

  <footer class="footer">
    <div class="brand"><span class="brand__mark"></span>TLHP QRF Realty</div>
    <div class="brand__site">TAMSWORTHLINDALE.EXAMPLE</div>
    <div class="divider"></div>
    <p class="invite">For more information or to schedule a private showing, contact Colette Varnum.</p>
    <p class="agent"><strong>Colette Varnum</strong><br><strong>REALTOR® License #3851207</strong><br>Tamsworth Lindale HomePartners<br>QRF Realty</p>
    <ul class="reach">
      <li><svg width="8" height="8" viewBox="0 0 10 10"><path d="M2 1l2 2-1 1.5a6 6 0 0 0 2.5 2.5L7 6l2 2-1.5 1.5C4 9 1 6 .5 2.5z" fill="#1b1f27"/></svg>555-208-4417</li>
      <li><svg width="8" height="8" viewBox="0 0 10 10" fill="none" stroke="#1b1f27"><rect x=".5" y="1.5" width="9" height="7"/><path d="M.5 1.5l4.5 4 4.5-4"/></svg>colettevarnum@mailbox.example</li>
      <li><svg width="8" height="8" viewBox="0 0 10 10" fill="none" stroke="#1b1f27"><path d="M5 9.5S1.5 6 1.5 3.8a3.5 3.5 0 0 1 7 0C8.5 6 5 9.5 5 9.5z"/><circle cx="5" cy="4" r="1.2"/></svg>480 Harbor Crest Way<br>Palmera Springs, FL 33902</li>
    </ul>
  </footer>
</section>

</body>
</html>
```